Business Card Design for Venture Lantern

Venture Lantern is a pro bono student consultancy service offered by Solvari KPTC to social start ups and enterprises. We provide consulting services with expertise in areas such as Marketing, IT, Business Strategy and Innovation.
I have attached\ the Venture Lantern Logo here for your perusal.
Industry/Entity Type
Business
Contact Information for Business Card
Name: Dae Hwan Park Name: Thomas Leung
Role: Project Leader Role: Vice Project Leader
M:0491203846 M: 0473560218
E: dae-hwan.park@solvarikptc.org E: thomas.leung@solvarikptc.org
W: www.solvarikptc.org W: www.solvarikptc.org

```html
<!DOCTYPE html>
<html lang="en">
<head>
<meta charset="utf-8">
<title>Venture Lantern – Business Card</title>
<link rel="stylesheet" href="https://fonts.googleapis.com/css2?family=Open+Sans:ital,wght@0,400;0,600;0,800;1,400;1,700&display=swap">
<style>
  :root {
    --orange: #e08a20;
    --paper: #f2f2f0;
    --ink: #1a1a1a;
    --faint: #c4c4c4;
    --white: #ffffff;
    --stage: #d9d9d9;
  }
  * { box-sizing: border-box; margin: 0; padding: 0; }
  html, body {
    width: 1200px; height: 1000px; overflow: hidden;
    background: var(--stage);
    font-family: "Open Sans", Arial, sans-serif;
  }
  .card {
    position: absolute; left: 210px;
    width: 780px; height: 446px;
    overflow: hidden;
    box-shadow: 0 2px 8px rgba(0,0,0,.15);
  }
  .card--front { top: 36px; background: var(--orange); }
  .card--back  { top: 518px; background: var(--paper); }
  .card-shapes { position: absolute; inset: 0; width: 100%; height: 100%; }

  .logo-panel {
    position: absolute; left: 240px; top: 118px;
    width: 300px; height: 210px;
    background: var(--paper);
    display: flex; align-items: center; justify-content: center;
  }
  .brand-name {
    font-weight: 800; text-transform: uppercase;
    text-align: center; line-height: 1.05; letter-spacing: -0.5px;
  }
  .logo-panel .brand-name { font-size: 40px; color: var(--ink); }
  .brand-name--faint {
    position: absolute; font-size: 34px; color: var(--faint);
  }
  .brand-name--top { left: 34px; top: 40px; }
  .brand-name--bottom { right: 34px; bottom: 34px; }

  .contact { position: absolute; color: var(--white); }
  .contact--lead { left: 470px; top: 62px; }
  .contact--vice { left: 40px; top: 236px; }
  .contact-name { font-size: 22px; font-weight: 700; font-style: italic; }
  .contact-role { font-size: 16px; font-style: italic; margin-bottom: 18px; }
  .contact-line { font-size: 16px; line-height: 1.6; }
</style>
</head>
<body>

<section class="card card--front" aria-label="Card front">
  <svg class="card-shapes" viewBox="0 0 780 446" aria-hidden="true">
    <polygon points="0,0 780,0 780,8 500,8 440,58 0,58" fill="var(--paper)"/>
    <polygon points="780,446 0,446 0,438 280,438 340,390 780,390" fill="var(--paper)"/>
  </svg>
  <div class="logo-panel">
    <p class="brand-name">Venture<br>Lantern</p>
  </div>
</section>

<section class="card card--back" aria-label="Card back">
  <svg class="card-shapes" viewBox="0 0 780 446" aria-hidden="true">
    <polygon points="0,190 230,225 500,0 780,0 780,300 590,270 300,446 0,446" fill="var(--orange)"/>
  </svg>

  <p class="brand-name brand-name--faint brand-name--top">Venture<br>Lantern</p>
  <p class="brand-name brand-name--faint brand-name--bottom">Venture<br>Lantern</p>

  <div class="contact contact--lead">
    <p class="contact-name">Dae Hwan Park</p>
    <p class="contact-role">Project Leader</p>
    <p class="contact-line">M : 049-120-3846</p>
    <p class="contact-line">E : dae-hwan.park@solvarikptc.org</p>
    <p class="contact-line">W : www.solvarikptc.org</p>
  </div>

  <div class="contact contact--vice">
    <p class="contact-name">Thomas Leung</p>
    <p class="contact-role">Vice Project Leader</p>
    <p class="contact-line">M : 047-356-0218</p>
    <p class="contact-line">E : thomas.leung@solvarikptc.org</p>
    <p class="contact-line">W : www.solvarikptc.org</p>
  </div>
</section>

</body>
</html>
```